Stationary Set and Logo Update **PAYMENT GUARANTEED**

Stationery Design and Logo Update

About Us

Trindex Supply is a wholesale distributor of OEM [original brand] and compatible [generic brand] parts and supplies for use in copiers, faxes, printers, and multi-function machines. In plain English…we sell all the parts and supplies [such as toner] that make up any office equipment which outputs an image on paper.

Trindex was the 1st distributor to develop and sell a generic brand copier part in the United States. We have been in business since 1972 [nearly 40 years]. Our tagline is "The Steady Choice," as in our company was the first alternative product that copier dealers had to buying original brand copier parts. Trindex is known for offering reliable and cost-effective OEM and compatible products.

Project

We require a fresh, modern and corporate identity. Please submit a stationary package inclusive of a double-sided business card (2" x 3.5"), letterhead (8.5'x11"), and standard #10 envelope (4-1/8” x 9-1/2). You may use our current logo or preferably your take on an updated one. If an attempt is made in updating the logo #004D8E or a similar hue should be used as the primary color.

The design should be clean, simple, modern and professional and make an immediate impact.

Target Market(s)

Copier and printer dealers who lease and service imaging equipment in the United States and Latin America.

Industry/Entity Type

Business

Requirements
Must have
• Simple, clean, modern and professional. Please use #004D8E or a similar hue as the primary color. Letterhead must accommate (2) addresses. We have 2 locations.
Nice to have
• A simple, modern update to our current logo. https://assets.mailvorbo.example/fs030/5520384417702/img/418.jpg
Should not have
• More than (2) colors on logo.

```html
<!DOCTYPE html>
<html lang="en">
<head>
<meta charset="utf-8">
<title>Trindex Supply Stationery Set</title>
<link href="https://fonts.googleapis.com/css2?family=Mulish:ital,wght@0,400;0,700;1,400&display=swap" rel="stylesheet">
<style>
  :root {
    --navy: #0b4f8c;
    --sky: #02a0d8;
    --ink: #1d2b3a;
    --stage: #f4f4f4;
    --paper: #ffffff;
    --edge: #222222;
  }
  * { box-sizing: border-box; margin: 0; padding: 0; }
  html, body { width: 1200px; height: 1019px; overflow: hidden; background: var(--paper); }
  body { position: relative; font-family: "Mulish", sans-serif; color: var(--ink); }
  .stage { position: absolute; left: 0; top: 0; width: 1200px; height: 915px; background: var(--stage); }
  .wordmark { position: absolute; font-weight: 700; color: var(--navy); letter-spacing: -0.5px; line-height: 1; white-space: nowrap; }
  .wordmark.light { color: var(--paper); }
  .hero-mark { left: 840px; top: 26px; font-size: 66px; }

  .sheet { position: absolute; background: var(--paper); border: 2px solid var(--edge); overflow: hidden; }
  .letterhead { left: 1px; top: 25px; width: 667px; height: 863px; }
  .card-front { left: 444px; top: 162px; width: 158px; height: 275px; }
  .card-back { left: 614px; top: 162px; width: 157px; height: 275px; background: var(--navy); border: none; }
  .envelope { left: 242px; top: 460px; width: 746px; height: 324px; }

  .band { position: absolute; }
  .band.navy { background: var(--navy); }
  .band.sky { background: var(--sky); }

  .office { position: absolute; font-size: 10px; line-height: 12px; color: var(--ink); }
  .office h3 { font-size: 13px; font-weight: 700; color: var(--sky); margin-bottom: 4px; line-height: 14px; }
  .office .label { font-style: italic; color: var(--sky); }
  .office .gap { margin-top: 3px; }

  .card-back .office { color: var(--paper); font-size: 8.5px; line-height: 11px; }
  .card-back .office h3 { color: var(--paper); font-size: 11px; margin-bottom: 2px; }
  .card-back .office .label { color: var(--paper); }

  .envelope .office { font-size: 8.5px; line-height: 10.5px; }
  .envelope .office h3 { font-size: 9.5px; margin-bottom: 2px; line-height: 11px; }
  .envelope .office .label { font-style: normal; }
  .divider { position: absolute; width: 2px; background: var(--sky); }

  .holder { position: absolute; left: 0; width: 100%; text-align: center; }
  .holder .name { font-size: 11px; font-weight: 700; color: var(--navy); }
  .holder .role { font-size: 11px; font-style: italic; color: var(--sky); }
</style>
</head>
<body>
  <div class="stage">
    <div class="wordmark hero-mark">Trindex</div>

    <section class="sheet letterhead">
      <div class="wordmark" style="left:30px;top:30px;font-size:30px;">Trindex</div>
      <div class="office" style="left:30px;top:107px;">
        <h3>Corporate Office</h3>
        <p>2270 Harbor Reach Avenue</p>
        <p>Coral Bend, FL 33390</p>
        <p class="gap"><span class="label">Toll Free:</span> 800.555.0142</p>
        <p><span class="label">Local:</span> 954.555.0186</p>
        <p><span class="label">Fax:</span> 954.555.0199</p>
      </div>
      <div class="office" style="left:31px;top:212px;">
        <h3>Trindex West</h3>
        <p>North Alder Commerce Park #7</p>
        <p>5512 Ridgeline Way</p>
        <p>Sparrow Flats, NV 89477</p>
        <p class="gap"><span class="label">Toll Free:</span> 800.555.0173</p>
        <p><span class="label">Fax:</span> 775.555.0128</p>
      </div>
      <div class="band navy" style="left:331px;top:790px;width:181px;height:73px;"></div>
      <div class="band sky" style="left:514px;top:790px;width:153px;height:73px;"></div>
    </section>

    <section class="sheet card-front">
      <div class="band sky" style="left:0;top:0;width:54px;height:23px;"></div>
      <div class="band navy" style="left:58px;top:0;width:60px;height:23px;"></div>
      <div class="wordmark" style="left:0;width:100%;text-align:center;top:56px;font-size:24px;">Trindex</div>
      <div class="holder" style="top:203px;">
        <p class="name">Marisol Trevane</p>
        <p class="role">Marketing Coordinator</p>
      </div>
      <div class="band navy" style="left:44px;top:248px;width:60px;height:25px;"></div>
      <div class="band sky" style="left:106px;top:248px;width:52px;height:25px;"></div>
    </section>

    <section class="sheet card-back">
      <div class="wordmark light" style="left:16px;top:56px;font-size:24px;">Trindex</div>
      <div class="office" style="left:16px;top:102px;">
        <h3>Trindex West</h3>
        <p>North Alder Commerce Park #7</p>
        <p>5512 Ridgeline Way</p>
        <p>Sparrow Flats, NV 89477</p>
        <p class="gap"><span class="label">Toll Free:</span> 800.555.0173</p>
        <p><span class="label">Fax:</span> 775.555.0128</p>
      </div>
      <div class="office" style="left:16px;top:184px;">
        <h3>Corporate Office</h3>
        <p>2270 Harbor Reach Avenue</p>
        <p>Coral Bend, FL 33390</p>
        <p class="gap"><span class="label">Toll Free:</span> 800.555.0142</p>
        <p><span class="label">Local:</span> 954.555.0186</p>
        <p><span class="label">Fax:</span> 954.555.0199</p>
      </div>
    </section>

    <section class="sheet envelope">
      <div class="wordmark" style="left:12px;top:13px;font-size:26px;">Trindex</div>
      <div class="divider" style="left:158px;top:7px;height:79px;"></div>
      <div class="office" style="left:167px;top:16px;">
        <h3>Corporate Office</h3>
        <p>2270 Harbor Reach Avenue</p>
        <p>Coral Bend, FL 33390</p>
        <p><span class="label">Toll Free:</span> 800.555.0142</p>
        <p><span class="label">Local:</span> 954.555.0186</p>
        <p><span class="label">Fax:</span> 954.555.0199</p>
      </div>
      <div class="divider" style="left:292px;top:7px;height:79px;"></div>
      <div class="office" style="left:300px;top:16px;">
        <h3>Trindex West</h3>
        <p>North Alder Commerce Park #7</p>
        <p>5512 Ridgeline Way</p>
        <p>Sparrow Flats, NV 89477</p>
        <p><span class="label">Toll Free:</span> 800.555.0173</p>
        <p><span class="label">Fax:</span> 775.555.0128</p>
      </div>
      <div class="band navy" style="left:515px;top:272px;width:122px;height:50px;"></div>
      <div class="band sky" style="left:640px;top:272px;width:104px;height:50px;"></div>
    </section>
  </div>
</body>
</html>
```